MD Business Card

I want to create a simple business card.
I am a consultant. I design and develop furniture, lighting and accessories for hospitality and retail brands.
I want the card to be simple and clean. Not too much of a logo - but it needs the basic information shown on the attached file.
Also - I have shown some fonts that I like on the attached file.
The card can be square or rectangle. It should be double sided.
I prefer 1-2 colors (not too colorful - but using color an an accent) Even if using color on the edges as an accent.

My snapquilt link shows some other graphics styles that I like. I like clean and simple.
http://www.snapquilt.com/marendowsett/business-cards/

Reason: I needed a few more days to see some of the options evolve.

Hospitality

```html
<!DOCTYPE html>
<html lang="en">
<head>
<meta charset="utf-8">
<title>maren dowsett hospitality &amp; home — business card</title>
<link rel="stylesheet" href="https://fonts.googleapis.com/css2?family=Cabin:wght@400;700&display=swap">
<style>
  :root {
    --paper: #ffffff;
    --ink: #111111;
    --accent: #5cc8c8;
  }
  html, body {
    margin: 0;
    padding: 0;
    width: 1200px;
    height: 741px;
    overflow: hidden;
    background: var(--paper);
  }
  .card {
    position: relative;
    width: 1200px;
    height: 741px;
    background: var(--paper);
    font-family: "Cabin", sans-serif;
    color: var(--ink);
  }
  .identity {
    position: absolute;
    left: 261px;
    width: 696px;
    top: 262px;
    margin: 0;
    text-align: center;
    font-size: 35px;
    line-height: 1;
    font-weight: 400;
    letter-spacing: 0.2px;
    white-space: nowrap;
  }
  .identity .name {
    font-weight: 700;
  }
  .rule {
    position: absolute;
    left: 261px;
    top: 314px;
    width: 696px;
    height: 2px;
    background: var(--accent);
  }
  .contact {
    position: absolute;
    left: 261px;
    width: 696px;
    top: 330px;
    margin: 0;
    display: flex;
    justify-content: space-between;
    align-items: baseline;
    font-size: 35px;
    line-height: 1;
    white-space: nowrap;
  }
  .contact .email {
    font-weight: 400;
  }
  .contact .phone {
    font-weight: 700;
    letter-spacing: 1px;
  }
</style>
</head>
<body>
  <main class="card">
    <h1 class="identity"><span class="name">maren dowsett</span> hospitality &amp; home</h1>
    <div class="rule"></div>
    <p class="contact">
      <span class="email">maren@marendowsett.com</span>
      <span class="phone">917.555.0142</span>
    </p>
  </main>
</body>
</html>
```